RB Cargonet businesscard project

RB Cargonet Ltd is a freshly founded small (3 employees), young (average age is 30 years) company, living from the road transportation market without own tools.
We would like to have an impressive, new-line, cool busines card for a freshly founded forwarding company on an overcrowded market which raises attention and makes the potential partners eager to work with us.

Our logo is in the attachment, please use it for the card.

Target Market(s)

The main profile of the company is logistic/forwarding on road.

Industry/Entity Type

Freight Forwarding

Contact Information for Business Card

Name: Varga Edina
Title: general manager
mobile nr: +36-70/482-5910
fax nr: +36-1/655-3947
e-mail: edina.varga@rbcargonet-example.com
info@rbcargonet-example.com
website address: http://www.rbcargonet-example.com
and if possible maybe some funny or helpful info on the back

Requirements
Must have
• contact details above
Nice to have
• some really nice and catching back-side (info, graphics, useful tool info... anything)
Should not have
• trucks, road, ship, airplane on it...

```html
<!DOCTYPE html>
<html lang="en">
<head>
<meta charset="utf-8">
<title>RB Cargonet – Business Card</title>
<link rel="stylesheet" href="https://fonts.googleapis.com/css2?family=Jost:wght@400;500&family=Oswald:wght@400&display=swap">
<style>
  :root {
    --stage: #474747;
    --card-white: #f7f7f7;
    --brand-blue: #527fb5;
    --ink-dark: #2f2f2f;
    --ink-soft: #5a5a5a;
    --white: #ffffff;
  }
  * { margin: 0; padding: 0; box-sizing: border-box; }
  html, body {
    width: 1200px;
    height: 750px;
    overflow: hidden;
    background: var(--stage);
  }
  .stage {
    position: relative;
    width: 1200px;
    height: 750px;
  }
  .card {
    position: absolute;
    top: 228px;
    width: 462px;
    height: 262px;
    overflow: hidden;
    font-family: "Jost", sans-serif;
  }
  .card-front { left: 124px; background: var(--card-white); }
  .card-back  { left: 618px; background: var(--brand-blue); }

  /* Front */
  .brand-square {
    position: absolute;
    left: 53px;
    top: 24px;
    width: 56px;
    height: 56px;
    background: var(--brand-blue);
  }
  .brand-name {
    position: absolute;
    left: 27px;
    top: 113px;
    font-family: "Oswald", sans-serif;
    font-weight: 400;
    font-size: 29px;
    letter-spacing: -0.3px;
    color: var(--ink-dark);
    white-space: nowrap;
  }
  .person {
    position: absolute;
    right: 24px;
    top: 22px;
    text-align: right;
  }
  .person-name {
    font-size: 22px;
    font-weight: 400;
    color: var(--brand-blue);
    line-height: 1.1;
    letter-spacing: 0.3px;
    white-space: nowrap;
  }
  .person-title {
    font-size: 14px;
    color: var(--ink-dark);
    line-height: 1.2;
    white-space: nowrap;
  }
  .accent-bar {
    position: absolute;
    right: 0;
    top: 27px;
    width: 8px;
    height: 34px;
    background: var(--brand-blue);
  }
  .contact-list {
    position: absolute;
    list-style: none;
    font-size: 11px;
    color: var(--ink-soft);
    line-height: 19.5px;
    white-space: nowrap;
  }
  .contact-company { left: 28px; top: 187px; }
  .contact-personal { right: 25px; top: 206px; text-align: right; }
  .contact-label {
    color: var(--brand-blue);
    font-weight: 500;
    margin-right: 2px;
  }

  /* Back */
  .back-name {
    position: absolute;
    left: 0;
    right: 0;
    top: 104px;
    text-align: center;
    font-weight: 500;
    font-size: 36px;
    color: var(--white);
    letter-spacing: 0.5px;
  }
  .back-web {
    position: absolute;
    left: 0;
    right: 0;
    top: 224px;
    text-align: center;
    font-size: 11.5px;
    letter-spacing: 4.5px;
    color: var(--white);
    white-space: nowrap;
  }
</style>
</head>
<body>
<main class="stage">
  <section class="card card-front" aria-label="Business card front">
    <div class="brand-square"></div>
    <div class="brand-name">RB Cargonet</div>

    <div class="person">
      <div class="person-name">Varga Edina</div>
      <div class="person-title">General Manager</div>
    </div>
    <div class="accent-bar"></div>

    <ul class="contact-list contact-company">
      <li><span class="contact-label">F :</span> +36-1/655-3947</li>
      <li><span class="contact-label">E :</span> info@rbcargonet-example.com</li>
      <li><span class="contact-label">W :</span> www.rbcargonet-example.com</li>
    </ul>

    <ul class="contact-list contact-personal">
      <li><span class="contact-label">M :</span> +36-70/482-5910</li>
      <li><span class="contact-label">E :</span> edina.varga@rbcargonet-example.com</li>
    </ul>
  </section>

  <section class="card card-back" aria-label="Business card back">
    <div class="back-name">RB Cargonet</div>
    <div class="back-web">www.rbcargonet-example.com</div>
  </section>
</main>
</body>
</html>
```